New Brochures to deliver confidence of our company to our customers

I would like to have new brochure to be used to distribute to our prospective customers besides the power point presentation. I like the powerpoint you did for us and would like to follow the direction that you have set up. I will attach a number of photos for you to include in our brochure for you to choose. I like the brochure to be modern and forward thinking but just practical. The brochure needs to have three languages which are English, Chinese and Japanese. Attaches is the power point that we like.

Target Market(s)

Multinational companies

Industry/Entity Type

Electronics

Colors

Designer to choose colors to be used in the design.

Requirements
Must have
• Feel lively and modern and yet giving people a sense of confidence. Highlighting the automation is important. Can let us know if you want more photos. The brochure will have three languages, namely english, japanese and chinese.

```html
<!DOCTYPE html>
<html lang="en">
<head>
<meta charset="utf-8">
<title>Norvale Circuits Limited – Brochure</title>
<link href="https://fonts.googleapis.com/css2?family=Roboto+Condensed:wght@300;400;700&family=Open+Sans:wght@400;600&display=swap" rel="stylesheet">
<style>
  :root{
    --green:#3aa647;
    --green-dark:#1f6b2c;
    --black:#111;
    --ink:#333;
    --muted:#777;
    --line:#2f7a3a;
    --paper:#fff;
    --bg:#e4e4e4;
    --table:#e6e6e6;
  }
  *{box-sizing:border-box;margin:0;padding:0}
  html,body{width:1200px;height:1200px;overflow:hidden;background:var(--bg)}
  body{font-family:"Open Sans",Arial,sans-serif;color:var(--ink)}
  .brochure{position:absolute;left:190px;top:30px;width:820px;height:1140px;background:var(--paper);overflow:hidden;box-shadow:0 4px 18px rgba(0,0,0,.18)}
  .header{position:absolute;left:0;top:0;width:820px;height:330px}
  .header svg{position:absolute;left:0;top:0}
  .header-photo{position:absolute;left:300px;top:0;width:520px;height:262px;background:linear-gradient(135deg,#c9cbc6,#8e918b 55%,#5d6a5e);clip-path:polygon(14% 0,100% 0,100% 100%,0 100%)}
  .brand{position:absolute;left:48px;top:175px}
  .brand-name{font-family:"Roboto Condensed",Arial,sans-serif;font-weight:700;font-size:58px;letter-spacing:4px;color:var(--green-dark);line-height:1}
  .brand-tag{font-family:"Roboto Condensed",Arial,sans-serif;font-weight:700;font-size:12px;letter-spacing:2.4px;color:var(--green-dark);margin-top:8px}
  .columns{position:absolute;top:345px;left:40px;width:750px;display:flex;gap:34px}
  .col{flex:1;min-width:0}
  h2{font-family:"Roboto Condensed",Arial,sans-serif;font-weight:400;color:var(--green-dark);font-size:17px;line-height:1.25;margin-bottom:5px}
  h2.small{font-size:13px}
  h2.one-line{font-size:14.5px;white-space:nowrap}
  p{font-size:9px;line-height:1.4;margin-bottom:4px}
  .lead::before{content:"> ";color:var(--green);font-weight:600}
  .lead .cap{font-size:13px}
  .share-table{width:100%;border-collapse:separate;border-spacing:0 2px;font-family:"Roboto Condensed",Arial,sans-serif;font-size:10px;color:var(--muted);margin:4px 0 8px}
  .share-table td,.share-table th{padding:2px 8px;font-weight:400;text-align:left}
  .share-table th{background:var(--table);font-size:11px}
  .share-table td:last-child,.share-table th:last-child{text-align:right;width:60px}
  .share-table tr:nth-child(odd) td{background:var(--table)}
  .framed{border:1.5px solid var(--line);border-radius:14px;padding:8px 12px 6px}
  .customers{position:absolute;left:40px;top:762px;width:750px;height:172px;border:1.5px solid var(--line);border-radius:16px;padding:10px 18px}
  .customers h2{font-size:19px;margin-bottom:3px}
  .customers .intro{font-size:9.5px;margin-bottom:8px}
  .logo-grid{display:grid;grid-template-columns:repeat(10,1fr);gap:8px}
  .partner{height:34px;border:1px solid #d4d4d4;border-radius:8px;box-shadow:0 1px 3px rgba(0,0,0,.12);display:flex;align-items:center;justify-content:center;font-family:"Open Sans",Arial,sans-serif;font-weight:600;font-size:10px;color:var(--ink)}
  .facility{position:absolute;left:40px;top:942px;width:750px}
  .facility h2{font-size:18px;margin-bottom:6px}
  .photo-row{display:flex;gap:8px;align-items:flex-end;height:94px}
  .photo{flex:1;height:70px;background:linear-gradient(140deg,#b8bdb5,#6f7a6d 60%,#3e5a41)}
  .photo:nth-child(2){height:75px}.photo:nth-child(3){height:80px}.photo:nth-child(4){height:85px}.photo:nth-child(5){height:90px}.photo:nth-child(6){height:94px}
  .footer{position:absolute;left:0;bottom:0;width:820px;height:70px}
  .footer svg{position:absolute;left:0;top:0}
  .footer-text{position:absolute;left:40px;top:18px;font-family:"Roboto Condensed",Arial,sans-serif;font-size:30px;letter-spacing:2px;color:#fff;white-space:nowrap}
</style>
</head>
<body>
<main class="brochure">
  <header class="header">
    <div class="header-photo" role="img" aria-label="Photo of the automated PCB production floor"></div>
    <svg width="820" height="330" viewBox="0 0 820 330" aria-hidden="true">
      <defs>
        <linearGradient id="panelGrad" x1="0" y1="0" x2="1" y2="1">
          <stop offset="0" stop-color="#ffffff"/>
          <stop offset=".55" stop-color="#a6d89c"/>
          <stop offset="1" stop-color="#3aa647"/>
        </linearGradient>
      </defs>
      <polygon points="0,110 300,110 420,262 360,330 0,330" fill="url(#panelGrad)"/>
      <polygon points="0,104 296,104 300,110 0,110" fill="#1f6b2c"/>
      <polygon points="300,262 820,262 820,278 360,278" fill="#1f6b2c"/>
      <polygon points="360,278 820,278 820,284 365,284" fill="#111"/>
    </svg>
    <div class="brand">
      <div class="brand-name">NCL</div>
      <div class="brand-tag">Printed Circuit Boards is Our Business</div>
    </div>
  </header>

  <section class="columns">
    <div class="col">
      <h2 class="small">NCL Background</h2>
      <p class="lead"><span class="cap">E</span>stablished in 2007, Norvale Circuits Limited (NCL) is a Hong Kong company specializing in single and double sided printed circuit boards. Its manufacturing facility is located in a self-owned facility in Tangxia, Dongguan of China which is 50 minutes from Hong Kong.</p>
      <p>Our mission is to become a premium low cost PCB supplier that fully embraces human, social and environmental responsibilities.</p>
      <p>Through our insatiable drive to maximize efficiency, NCL is becoming a highly efficient PCB factory with a capacity of 140,000 sq meter a month.</p>
      <p>PCB is our business and it is through continued automation and innovation that will drive our growth in the next 10 years.</p>
      <h2>Our investment and upgrade</h2>
      <p class="lead"><span class="cap">M</span>aintaining a highly automated factory is the only way to ensure consistent product and long term competitive efficiency.</p>
      <p>From 2015 to 2017, NCL invested over US$3.5 million in automating our production and quality control process and enhancing our environmental processing facility. We will spend a further US$1.5 million in 2018 to continue our improvement process to ensure we are one of the most efficient and highest quality single sided PCB manufacturers in Asia.</p>
      <p>By the end of 2018, 100% of our PCBs will be inspected by AVI before they are delivered to our customers.</p>
    </div>
    <div class="col">
      <h2>Single Layered Printed Circuit Boards</h2>
      <p class="lead"><span class="cap">W</span>e are offering single layered circuit boards through our own production facility in China for customers in the following industries:</p>
      <table class="share-table">
        <tr><th>Application</th><th>比例 %</th></tr>
        <tr><td>Household appliances</td><td>50%</td></tr>
        <tr><td>Power supply</td><td>20%</td></tr>
        <tr><td>Lighting control system</td><td>10%</td></tr>
        <tr><td>others</td><td>10%</td></tr>
      </table>
      <h2 class="one-line">Double Layered And Multi-layered Printed Circuit Boards</h2>
      <div class="framed">
        <p class="lead"><span class="cap">W</span>e are offering two layered and multi-layered circuit boards for our customers through our strategically approved printed circuit boards manufacturers.</p>
        <p>With our own UL for double sided and multi-layered circuit boards, we work with a number of strategically approved manufacturers in delivering 100% quality guaranteed printed circuit boards for our customers.</p>
        <p>All the PCBs are inspected by our own Automatic Visual Inspection (AVI) Machine before we deliver to customers.</p>
        <p>We perform comprehensive quality and environmental audit of our manufacturers on quarterly and annual basis.</p>
      </div>
    </div>
  </section>

  <section class="customers">
    <h2>Customers</h2>
    <p class="intro">NCL is embracing a philosophy of being a partner with our customers. As a result, we are strategic PCB suppliers to the following world renowned companies:</p>
    <div class="logo-grid">
      <div class="partner">Torvik</div><div class="partner">Veltmann</div><div class="partner">Kaminos</div><div class="partner">Kestrel</div><div class="partner">Moldura</div><div class="partner">Vantor</div><div class="partner">Brevik</div><div class="partner">Miroku</div><div class="partner">Fenwa</div><div class="partner">Halden</div>
      <div class="partner">Altrion</div><div class="partner">Sevra</div><div class="partner">Ashgrove</div><div class="partner">Kelmar</div><div class="partner">Orvane</div><div class="partner">Halco</div><div class="partner">Tesson</div><div class="partner">Deltrix</div><div class="partner">Lumeo</div><div class="partner">Quinta</div>
    </div>
  </section>

  <section class="facility">
    <h2>Show pictures of the facility.</h2>
    <div class="photo-row">
      <div class="photo" role="img" aria-label="Facility photo: PCB coating machine"></div>
      <div class="photo" role="img" aria-label="Facility photo: automated conveyor line"></div>
      <div class="photo" role="img" aria-label="Facility photo: plating racks"></div>
      <div class="photo" role="img" aria-label="Facility photo: drilling machines"></div>
      <div class="photo" role="img" aria-label="Facility photo: inspection station"></div>
      <div class="photo" role="img" aria-label="Facility photo: production line overview"></div>
    </div>
  </section>

  <footer class="footer">
    <svg width="820" height="70" viewBox="0 0 820 70" aria-hidden="true">
      <rect x="0" y="0" width="820" height="70" fill="#3aa647"/>
      <polygon points="700,0 820,0 820,70 760,70" fill="#111"/>
    </svg>
    <div class="footer-text">Norvale Circuits Limited &nbsp;|&nbsp; www.norvalecircuits.com</div>
  </footer>
</main>
</body>
</html>
```